New Toothpaste brand needs a logo & packaging design

Our company is launching a new toothpaste and is looking for a logo and packaging design. The toothpaste brand is called Brivana. The packaging should have the same design quality as the major international brands, such as Lumora, Lumora Totalcare, Dentiva, Pexolo, Wind-rise, Marvest, etc. The dominant colors for our brand should be hues of blue, similar to other major brands. In addition, there should be a little bit of green to represent the "Fresh Mint Blast" flavor and the "Extracts of Aloe Vera" included in the ingredients.

There are typically 3 unique sides on a toothpaste box:

The face: Repeated on ~3 sides of the 4 faces of the box
The back: The 4th box face has the instructions for use, ingredients, company information, bar code/product info, and some branding elements.
The sides: Usually consisting of just the logo, flavor etc.

Please refer to existing brands such as Lumora, Lumora Total-care, and Dentiva for an example of typical box layout and elements.

Task Details:
Package Dimensions: 180 mm x 48 mm x 28 mm, 100 ml toothpaste tube
Brand Name: Brivana
Description: Fluoride Toothpaste
Flavor: Fresh Mint Blast
5 Actions: Protects against cavities and tartar, freshens breath, whitens teeth, and maintains healthy gums. These actions can also be made into a list like Lumora Total Care or Dentiva Max care. For instance, Strong Teeth, Fresh Breath, Whitening, Healthy Gums, Cavity and Tartar Protection.
Also contains whitening micro particles and extracts of aloe vera which may be highlighted on the package

Overall, the look should be high quality and with the same look and feel as the big brands mentioned previously. We do not have an existing logo for this brand. The face of the package is the most important element as it is often repeated on several sides and on the tube itself.

Please let me know if you have any questions.

I've attached some of our favorite big brand designs below. I would say the Lumora Total Care and Gleam vers

The logos I've seen so far for Brivana, have been a bit too bold. A little bold is okay, but just needs to be moderate. 

I would like the colors to be bright and appealing. I mentioned shades of blue being the major color, but green should also be highlighted as well, perhaps in a 80% blue to 20% green ratio. 

Target Market(s)

adult consumer of toothpaste, both female and male.

Industry/Entity Type

It Company

Requirements
Must have
• A logo with the brand name: Brivana
Description or sub text: Fluoride Toothpaste
Flavor: Fresh Mint Blast
A phrase or list describing the Toothpaste Actions: e.g., Protects against cavities and tartar, freshens breath, whitens teeth, and maintains healthy gums. Or as a list simialr to Lumora Total Care or Dentiva Max Care:
-Anti-cavity
-Anti-tartar
-Fresh breath
-Whitening
-Healthy Gums

Special ingredient of "whitening micro particles: and "extracts of aloe vera", which should also be highlighted.

The color should mostly be shades of blue, with only a little bit of green to accentuate the fresh mint blast flavor and aloe vera

Nice to have
• The design should really look good next to lumora total care, gleam pure, and dentiva max care. These are our favorite designs.
Should not have
• For aloe vera, there is no need to show the plant.

The Brivana logo shouldn't be too Bold. This should be appeal to all consumers, not just men.

```html
<!DOCTYPE html>
<html lang="en">
<head>
<meta charset="utf-8">
<title>Brivana Fluoride Toothpaste – Box Face</title>
<link rel="stylesheet" href="https://fonts.googleapis.com/css2?family=Open+Sans:ital,wght@0,400;0,600;0,700;0,800;1,400;1,600;1,700;1,800&display=swap">
<style>
  :root {
    --brand-blue: #5b96cf;
    --navy: #1c3577;
    --deep-navy: #213d8c;
    --sky: #a9c7e8;
    --mid-blue: #649fd6;
    --mint: #17907a;
    --alert-red: #d8232a;
    --silver-light: #f4f4f4;
    --silver: #cfcfcf;
    --white: #ffffff;
  }
  * { margin: 0; padding: 0; box-sizing: border-box; }
  html, body { width: 1200px; height: 314px; overflow: hidden; background: var(--white); }
  .box-face {
    position: relative;
    width: 1200px;
    height: 314px;
    overflow: hidden;
    font-family: "Open Sans", Arial, sans-serif;
  }
  .box-art { position: absolute; inset: 0; }
  .label { position: absolute; white-space: nowrap; }
  .new-flag {
    left: 14px; top: 5px;
    color: var(--white); font-weight: 800; font-style: italic; font-size: 27px;
  }
  .tagline {
    left: 380px; top: 3px;
    color: var(--navy); font-style: italic; font-weight: 400;
    font-size: 27px; letter-spacing: 18px;
  }
  .brand-name {
    left: 140px; top: 50px;
    color: var(--brand-blue); font-weight: 600; font-size: 114px;
    letter-spacing: 6px; line-height: 1;
  }
  .product-type {
    left: 218px; top: 170px;
    color: var(--navy); font-weight: 800; font-style: italic;
    font-size: 33px; letter-spacing: 1px;
  }
  .flavour {
    left: 258px; top: 216px;
    color: var(--white); font-weight: 700; font-style: italic; font-size: 24px;
  }
  .volume {
    left: 32px; top: 262px;
    color: var(--white); font-size: 21px; font-weight: 400;
  }
  .benefit-list {
    position: absolute; left: 944px; top: 50px;
    list-style: none;
    color: var(--navy); font-weight: 700; font-style: italic; font-size: 18px; line-height: 24px;
  }
  .benefit-list li::before { content: "• "; color: var(--alert-red); }
  .benefit-list li:nth-child(2) { padding-left: 14px; }
  .benefit-list li:nth-child(3) { padding-left: 40px; }
  .benefit-list li:nth-child(4) { padding-left: 50px; }
  .benefit-list li:nth-child(5) { padding-left: 46px; }
  .combo-badge {
    left: 1000px; top: 190px;
    color: var(--white); font-weight: 800; font-style: italic; font-size: 42px; line-height: 1;
  }
  .combo-badge small { font-size: 30px; }
</style>
</head>
<body>
<div class="box-face">
  <svg class="box-art" width="1200" height="314" viewBox="0 0 1200 314">
    <defs>
      <linearGradient id="blueField" x1="0" x2="1" y1="0" y2="0">
        <stop offset="0" stop-color="var(--mid-blue)"/>
        <stop offset="0.55" stop-color="var(--sky)"/>
        <stop offset="1" stop-color="var(--deep-navy)"/>
      </linearGradient>
      <linearGradient id="silverBand" x1="0" x2="1" y1="0" y2="0">
        <stop offset="0" stop-color="var(--silver)"/>
        <stop offset="0.5" stop-color="var(--silver-light)"/>
        <stop offset="1" stop-color="var(--silver)"/>
      </linearGradient>
      <radialGradient id="toothGlow" cx="0.45" cy="0.4" r="0.7">
        <stop offset="0" stop-color="#ffffff"/>
        <stop offset="1" stop-color="#7fb0e0"/>
      </radialGradient>
      <linearGradient id="waveTones" x1="0" x2="0" y1="0" y2="1">
        <stop offset="0" stop-color="#ffffff"/>
        <stop offset="0.5" stop-color="#2aa08a"/>
        <stop offset="1" stop-color="#5b96cf"/>
      </linearGradient>
      <path id="badgeArc" d="M770,150 A98,98 0 0 0 966,150"/>
    </defs>

    <rect width="1200" height="314" fill="var(--white)"/>
    <rect y="168" width="1200" height="146" fill="url(#blueField)"/>
    <rect width="1200" height="44" fill="url(#silverBand)"/>
    <polygon points="0,0 128,0 100,44 0,44" fill="var(--alert-red)"/>

    <polygon points="140,168 790,168 790,212 182,212" fill="url(#silverBand)"/>
    <polygon points="182,212 790,212 790,252 222,252" fill="var(--mint)"/>
    <path d="M700,210 C702,188 720,176 746,174 C744,196 728,210 700,210 Z" fill="var(--mint)" stroke="var(--white)" stroke-width="3"/>

    <circle cx="868" cy="150" r="106" fill="var(--white)"/>
    <circle cx="868" cy="150" r="102" fill="var(--mint)"/>
    <path d="M766,150 A102,102 0 0 0 970,150 Z" fill="#e9eef3"/>
    <circle cx="868" cy="150" r="78" fill="url(#toothGlow)" stroke="var(--white)" stroke-width="3" role="img" aria-label="Illustration of a shining white tooth inside a glossy bubble"/>
    <text font-family="Open Sans, Arial, sans-serif" font-weight="700" font-size="15" fill="var(--navy)" letter-spacing="1">
      <textPath href="#badgeArc" startOffset="50%" text-anchor="middle">WHITENING MICRO PARTICLES</textPath>
    </text>

    <rect x="986" y="190" width="150" height="52" rx="14" fill="var(--alert-red)" stroke="var(--white)" stroke-width="3"/>
    <rect x="984" y="246" width="192" height="46" rx="20" fill="url(#waveTones)" role="img" aria-label="Flowing stripes of white, mint and blue toothpaste"/>
  </svg>

  <span class="label new-flag">NEW</span>
  <span class="label tagline">COMPLETE PROTECTION</span>
  <span class="label brand-name">BRIVANA</span>
  <span class="label product-type">FLUORIDE TOOTHPASTE</span>
  <span class="label flavour">Fresh Mint Blast with extracts of aloe vera</span>
  <span class="label volume">100 ml</span>

  <ul class="benefit-list">
    <li>Anti-cavity</li>
    <li>Anti-tartar</li>
    <li>Fresh breath</li>
    <li>Whitening</li>
    <li>Healthy Gums</li>
  </ul>

  <span class="label combo-badge">5<small>in</small>1</span>
</div>
</body>
</html>
```